Banner Design for Physiotherapy Business

I need a banner designed for a physiotherapy business. The word ‘Physiotherapy’ should be prominent at the top. I’ve attached a document outlining what text and a suggestion of a picture I’d like included. The photo I have suggested in the document won’t upload to plumvista though as the dimensions are too large. I am open to other photos being used though. I would like to see designs that use the colour orange (as seen in the example) or green preferrably. The dimensions need to be 841mm x 2055mm and provided in PDF, JPG, and PNG format and 300dpi in CMYK colour mode.

```html
<!DOCTYPE html>
<html lang="en">
<head>
<meta charset="utf-8">
<title>Physiotherapy Banner</title>
<link rel="stylesheet" href="https://fonts.googleapis.com/css2?family=Oswald:wght@300;400;600;700&family=Roboto+Condensed:wght@400&family=Montserrat:wght@700;800&display=swap">
<style>
  :root {
    --sky: #00b0ee;
    --navy: #0a6ebd;
    --ring: #3fc2f5;
    --white: #ffffff;
    --ink: #111111;
    --stage: #8c8c8c;
  }
  * { margin: 0; padding: 0; box-sizing: border-box; }
  html, body { width: 1200px; height: 1080px; overflow: hidden; background: var(--stage); }
  .banner-frame {
    position: absolute; left: 391px; top: 30px;
    width: 417px; height: 1020px; overflow: hidden;
    box-shadow: 0 6px 18px rgba(0,0,0,.35);
  }
  .banner {
    position: absolute; left: 0; top: 0;
    width: 620px; height: 1515px;
    transform: scale(0.673); transform-origin: 0 0;
    background: var(--sky); overflow: hidden;
  }
  .banner-art { position: absolute; inset: 0; }
  .headline {
    position: absolute; left: 0; right: 0; top: 48px;
    text-align: center; color: var(--white);
    font-family: "Oswald", sans-serif; font-weight: 700;
    font-size: 92px; line-height: 1; letter-spacing: -1px;
    transform: scaleX(0.86);
  }
  .section-title {
    position: absolute; left: 58px; width: 504px; top: 686px;
    color: var(--white); font-family: "Oswald", sans-serif;
    font-size: 76px; line-height: 1; text-align: center;
    border-bottom: 3px solid var(--white); padding-bottom: 10px;
  }
  .section-title .light { font-weight: 300; }
  .section-title .bold { font-weight: 700; }
  .treat-list {
    position: absolute; list-style: none; color: var(--white);
    font-family: "Roboto Condensed", sans-serif; font-size: 25px;
  }
  .treat-list li { position: relative; padding-left: 32px; }
  .treat-list li::before {
    content: ""; position: absolute; left: 0; top: 7px;
    width: 18px; height: 18px; border: 1.5px solid var(--white); border-radius: 50%;
  }
  .treat-list li::after {
    content: ""; position: absolute; left: 5px; top: 11px;
    width: 8px; height: 4px; border-left: 1.5px solid var(--white); border-bottom: 1.5px solid var(--white);
    transform: rotate(-45deg);
  }
  .treat-list.left { left: 54px; top: 796px; }
  .treat-list.left li { height: 44.3px; line-height: 32px; }
  .treat-list.right { left: 329px; top: 795px; width: 260px; line-height: 34px; }
  .treat-list.right li { margin-bottom: 9px; }
  .partner-badge {
    position: absolute; left: 50px; top: 1252px;
    width: 112px; height: 84px; border-radius: 50%;
    background: var(--ring);
  }
  .booking { position: absolute; left: 343px; top: 1247px; }
  .booking-tag {
    display: inline-block; background: var(--ink); color: var(--white);
    font-family: "Oswald", sans-serif; font-weight: 600; font-size: 23px;
    padding: 0 10px; height: 35px; line-height: 35px;
  }
  .booking-address {
    margin-top: 14px; padding-left: 10px; color: var(--white);
    font-family: "Montserrat", sans-serif; font-weight: 700;
    font-size: 17px; line-height: 21.5px; font-style: normal;
  }
  .phone-pill {
    position: absolute; left: 45px; top: 1402px; width: 530px; height: 72px;
    background: var(--white); border: 3px solid var(--navy); border-radius: 36px;
    display: flex; align-items: center; gap: 18px; padding-left: 28px;
  }
  .phone-number {
    font-family: "Montserrat", sans-serif; font-weight: 800;
    font-size: 50px; color: var(--ink); letter-spacing: -1px;
  }
</style>
</head>
<body>
  <div class="banner-frame">
    <div class="banner">
      <svg class="banner-art" width="620" height="1515" viewBox="0 0 620 1515">
        <defs>
          <linearGradient id="photoTone" x1="0" y1="0" x2="1" y2="1">
            <stop offset="0" stop-color="#f4f6f8"/>
            <stop offset="0.55" stop-color="#dfe3e8"/>
            <stop offset="1" stop-color="#a9b3bf"/>
          </linearGradient>
        </defs>
        <circle cx="383" cy="477" r="335" fill="none" stroke="var(--white)" stroke-width="3"/>
        <circle cx="338" cy="482" r="323" fill="url(#photoTone)" role="img" aria-label="Photo: physiotherapist guiding a senior patient through an arm exercise with a small dumbbell"/>
        <circle cx="310" cy="980" r="452" fill="none" stroke="var(--ring)" stroke-width="3"/>
        <circle cx="310" cy="972" r="427" fill="var(--navy)"/>
        <path d="M0 1235 Q310 1470 620 1330" fill="none" stroke="var(--white)" stroke-width="2"/>
      </svg>

      <h1 class="headline">PHYSIOTHERAPY</h1>

      <h2 class="section-title"><span class="light">WHAT WE</span> <span class="bold">TREAT</span></h2>

      <ul class="treat-list left">
        <li>Arthritis</li>
        <li>Sciatic pain</li>
        <li>Repetitive strain injuries</li>
        <li>Tennis elbow</li>
        <li>Postural pain</li>
        <li>Workplace injuries</li>
        <li>Motor vehicle accidents</li>
        <li>Women’s health issues</li>
        <li>Clinical exercise</li>
      </ul>

      <ul class="treat-list right">
        <li>Back pain / Neck pain</li>
        <li>Sports injuries</li>
        <li>Post surgical management (hip and knee arthroscopes, joint replacement surgery)</li>
        <li>Pre-employment functional assessments</li>
        <li>Shoulder pain and dysfunction</li>
      </ul>

      <div class="partner-badge" role="img" aria-label="Professional association membership badge"></div>

      <div class="booking">
        <div class="booking-tag">MAKE AN APPOINTMENT</div>
        <address class="booking-address">Kellbrook Family Practice<br>18-20 Marlow St<br>Kellbrook VIC 3199</address>
      </div>

      <div class="phone-pill">
        <svg width="52" height="52" viewBox="0 0 52 52" aria-hidden="true">
          <path d="M14 6 L21 15 Q22 18 19 20 L16 22 Q20 31 29 36 L32 33 Q34 31 37 32 L46 39 Q47 42 44 45 L41 47 Q34 49 24 42 Q12 33 6 20 Q3 12 8 8 Z" fill="none" stroke="var(--navy)" stroke-width="3" stroke-linejoin="round"/>
          <path d="M30 6 Q44 8 46 22 M29 12 Q39 14 40 23 M28 18 Q33 19 34 24" fill="none" stroke="var(--navy)" stroke-width="2.5" stroke-linecap="round"/>
        </svg>
        <span class="phone-number">(03) 9000 4821</span>
      </div>
    </div>
  </div>
</body>
</html>
```